Modern and strong website design for a Dutch crowdsourcing company
.

We are startup company providing crowdsourcing of administrative and customers service tasks for larger companies and other organizations. We offer cost savings and scale-ability combined with higher quality of execution. We will soon enter the market and need a website that has two major target groups: 1. Our corporate customers 2. The mainly younger crowd executing the tasks on our platform.
The target group of customers are Influencers and decision makers with companies and other organizations in with large administrative and customer service departments. Most information in the startup phase will be targeting this group.
The target group of future crowd workers will be heterogeneous, from students to stay at home mums or night shift workers who want to earn some extra money by performing easy to execute microtasks in the cloud. We will target both Dutch and international workers.

The website must be developed for browsing on a computer but also be optimized for mobile devices and tablets.
The website must be optimized and tested for the major browsers on windows, macOS and mobile devices.

For the minimum requirement for the website see attached wireframes

The present landing page http://bravolinkhive.com and logo are not reflecting our preferences!
See enclosed a new logo that stands for both the crowdwork (performed for our customers) and the crowd (a hive in motion).

Target Market(s)

see tekst above.

Industry/Entity Type

Business Service

Coding

Coded - Design and coding required

Number of Pages Required

5+ page

Font styles to use
Sans Serif
Other font styles liked:
• Lato, Open Sans

Colors

Designer to choose colors to be used in the design.

Requirements
Must have
• start devider screen
• home page displaying business and worker information
• a page displaying only info for businesses
• a page displaying only info for workers
• a contact form
• a reviews page
• color scheme from logo
• responsiveness!
Nice to have
• Nice animations
• overlapping blocks, animated on scroll
• lightbox effects if applicable
• animated mobile menu icon and menu itself

```html
<!DOCTYPE html>
<html lang="en">
<head>
<meta charset="utf-8">
<title>References – A Hive in Motion</title>
<link href="https://fonts.googleapis.com/css2?family=Jost:wght@400;500;600&display=swap" rel="stylesheet">
<style>
:root{
  --orange:#f07c00;
  --ink:#2b2b2b;
  --text:#3a3a3a;
  --muted:#9a9a9a;
  --line:#e2e2e2;
  --footer:#0d0d0d;
  --white:#fff;
}
*{margin:0;padding:0;box-sizing:border-box}
html,body{width:816px;height:1200px;overflow:hidden;background:var(--white)}
body{font-family:"Jost",sans-serif;color:var(--text);position:relative}
.site-header{position:absolute;left:0;top:0;width:816px;height:66px;background:var(--white)}
.topbar-strip{position:absolute;left:0;top:0;width:816px;height:3px;background:var(--orange)}
.topbar{position:absolute;left:510px;top:0;width:306px;height:23px;background:var(--orange);
  border-bottom-left-radius:4px;display:flex;align-items:center;color:var(--white);font-size:10px;padding-left:20px;gap:22px}
.topbar span{display:flex;align-items:center;gap:8px}
.icon-dot{width:14px;height:14px;border-radius:50%;background:rgba(255,255,255,.3);display:inline-flex;align-items:center;justify-content:center}
.mail{position:absolute;left:352px;top:6px;font-size:10px;color:var(--ink);display:flex;align-items:center;gap:8px}
.mail .icon-dot{background:#c9c9c9}
.brand{position:absolute;left:60px;top:18px;display:flex;align-items:center;gap:8px;font-size:22px;font-weight:600;color:var(--ink)}
.brand-dot{width:14px;height:14px;border-radius:50%;background:var(--orange)}
.nav{position:absolute;top:43px;left:453px;display:flex;gap:0;font-size:9.5px;font-weight:500;color:var(--ink)}
.nav a{color:inherit;text-decoration:none;margin-right:42px}
.nav a:last-child{margin-right:0}
.hero{position:absolute;left:0;top:66px;width:816px;height:203px;
  background:linear-gradient(90deg,#d6dcdc 0%,#e9ecea 30%,#c9cdcf 55%,#3b55a8 62%,#5a6fb3 72%,#e9e9e6 85%,#b8c2b6 100%)}
.breadcrumb{position:absolute;left:0;top:269px;width:816px;height:26px;border-bottom:1px solid var(--line);
  display:flex;align-items:center;padding-left:60px;gap:12px;font-size:9px;color:var(--orange)}
.breadcrumb .sep{color:var(--ink)}
.page-title{position:absolute;left:0;top:326px;width:816px;text-align:center;font-size:23px;font-weight:500;color:var(--orange);letter-spacing:.3px}
.divider{position:absolute;left:310px;top:368px;width:196px;height:16px}
.references{position:absolute;left:60px;top:401px;width:696px}
.ref-card{height:113px;margin-bottom:14px;background:var(--white);box-shadow:0 0 4px rgba(0,0,0,.14);position:relative}
.ref-card:nth-child(2){margin-bottom:14px}
.ref-client{position:absolute;left:8px;top:0;width:90px;height:113px;display:flex;flex-direction:column;align-items:center;justify-content:center;gap:6px;
  font-size:12px;font-weight:600;color:#333;letter-spacing:1px}
.ref-client i{width:18px;height:18px;background:#444;display:block}
.quote{position:absolute;left:102px;top:18px;width:14px;height:10px;color:#ccc;font-size:22px;line-height:10px;font-weight:600}
.ref-body{position:absolute;left:119px;top:17px;width:556px;font-size:9.6px;line-height:15.8px;color:var(--text)}
.ref-author{position:absolute;left:117px;top:86px;font-size:9.6px;color:var(--orange)}
.site-footer{position:absolute;left:0;top:1060px;width:816px;height:140px;background:var(--footer);color:var(--white)}
.footer-nav{position:absolute;top:26px;width:816px;text-align:center;font-size:10px}
.footer-nav .slash{margin:0 9px}
.social{position:absolute;top:61px;left:342px;display:flex;gap:6px}
.social span{width:21px;height:21px;border-radius:50%;background:var(--white);display:block}
.social span:first-child{background:var(--orange)}
.copyright{position:absolute;top:103px;width:816px;text-align:center;font-size:8px}
</style>
</head>
<body>
<header class="site-header">
  <div class="topbar-strip"></div>
  <div class="mail"><i class="icon-dot"><svg width="8" height="6" viewBox="0 0 8 6"><rect x=".5" y=".5" width="7" height="5" fill="none" stroke="#fff"/><path d="M.5 .5 4 3.5 7.5 .5" fill="none" stroke="#fff"/></svg></i>Mail Us : info@hiveinmotion.com</div>
  <div class="topbar">
    <span><i class="icon-dot"><svg width="7" height="7" viewBox="0 0 10 10"><path d="M2 0 4 3 3 4Q4 6 6 7L7 6 10 8 8 10Q2 9 0 2Z" fill="#fff"/></svg></i>Call Us : (123) 555-0199</span>
    <span><i class="icon-dot"><svg width="7" height="7" viewBox="0 0 10 10"><circle cx="5" cy="3" r="2.5" fill="#fff"/><path d="M0 10Q5 3 10 10Z" fill="#fff"/></svg></i>For Workers</span>
  </div>
  <div class="brand"><i class="brand-dot"></i>A Hive in Motion</div>
  <nav class="nav"><a>HOME</a><a>FOR BUSINESS</a><a>REVIEWS</a><a>GET IN CONTACT</a></nav>
</header>

<div class="hero" role="img" aria-label="Photo of three colleagues reviewing work together at an office desk"></div>

<div class="breadcrumb">
  <svg width="10" height="9" viewBox="0 0 10 9"><path d="M5 0 10 4.5H8.5V9H6V6H4V9H1.5V4.5H0Z" fill="#2b2b2b"/></svg>
  <span class="sep">»</span><span>REFERENCES</span>
</div>

<h1 class="page-title">REFERENCES</h1>
<svg class="divider" viewBox="0 0 196 16"><line x1="0" y1="8" x2="82" y2="8" stroke="#ccc"/><line x1="114" y1="8" x2="196" y2="8" stroke="#ccc"/><circle cx="98" cy="8" r="6" fill="none" stroke="#bbb" stroke-width="2"/></svg>

<main class="references">
  <article class="ref-card">
    <div class="ref-client"><i></i>STONEFIELD</div>
    <span class="quote">“</span>
    <p class="ref-body">Nemo enim ipsam voluptatem quia voluptas sit aspernatur aut odit aut fugit, sed quia labore consequuntur magni dolores eos qui ratione incididted voluptatem sequi nesciunt. Neque this porro quisquam est, qui dolorem ipsum quia dolor sit amet, consectetur, adipisci velit, sedest quia non numquam eius modi tempora incidunt ut labore ets to dolore magnam aliquams this quaerat voluptatem eu fugiat nulla pariatur. Excepteur sint occaecat cupidatat non proident, sunt in culpa qui officia deserunt mollit anim id est laborum ”</p>
    <span class="ref-author">By Daniel K.</span>
  </article>
  <article class="ref-card">
    <div class="ref-client"><i></i>OAKBUILD</div>
    <span class="quote">“</span>
    <p class="ref-body">Nemo enim ipsam voluptatem quia voluptas sit aspernatur aut odit aut fugit, sed quia labore consequuntur magni dolores eos qui ratione incididted voluptatem sequi nesciunt. Neque this porro quisquam est, qui dolorem ipsum quia dolor sit amet, consectetur, adipisci velit, sedest quia non numquam eius modi tempora incidunt ut labore ets to dolore magnam aliquams this quaerat voluptatem eu fugiat nulla pariatur. Excepteur sint occaecat cupidatat non proident, sunt in culpa qui officia deserunt mollit anim id est laborum</p>
    <span class="ref-author">By Daniel K.</span>
  </article>
  <article class="ref-card">
    <div class="ref-client"><i></i>HARBORLINE</div>
    <span class="quote">“</span>
    <p class="ref-body">Nemo enim ipsam voluptatem quia voluptas sit aspernatur aut odit aut fugit, sed quia labore consequuntur magni dolores eos qui ratione incididted voluptatem sequi nesciunt. Neque this porro quisquam est, qui dolorem ipsum quia dolor sit amet, consectetur, adipisci velit, sedest quia non numquam eius modi tempora incidunt ut labore ets to dolore magnam aliquams this quaerat voluptatem eu fugiat nulla pariatur. Excepteur sint occaecat cupidatat non proident, sunt in culpa qui officia deserunt mollit anim id est laborum</p>
    <span class="ref-author">By Daniel K.</span>
  </article>
  <article class="ref-card">
    <div class="ref-client"><i></i>NETWISE</div>
    <span class="quote">“</span>
    <p class="ref-body">Nemo enim ipsam voluptatem quia voluptas sit aspernatur aut odit aut fugit, sed quia labore consequuntur magni dolores eos qui ratione incididted voluptatem sequi nesciunt. Neque this porro quisquam est, qui dolorem ipsum quia dolor sit amet, consectetur, adipisci velit, sedest quia non numquam eius modi tempora incidunt ut labore ets to dolore magnam aliquams this quaerat voluptatem eu fugiat nulla pariatur. Excepteur sint occaecat cupidatat non proident, sunt in culpa qui officia deserunt mollit anim id est laborum</p>
    <span class="ref-author">By Daniel K.</span>
  </article>
  <article class="ref-card">
    <div class="ref-client"><i></i>LUMENHAUS</div>
    <span class="quote">“</span>
    <p class="ref-body">Nemo enim ipsam voluptatem quia voluptas sit aspernatur aut odit aut fugit, sed quia labore consequuntur magni dolores eos qui ratione incididted voluptatem sequi nesciunt. Neque this porro quisquam est, qui dolorem ipsum quia dolor sit amet, consectetur, adipisci velit, sedest quia non numquam eius modi tempora incidunt ut labore ets to dolore magnam aliquams this quaerat voluptatem eu fugiat nulla pariatur. Excepteur sint occaecat cupidatat non proident, sunt in culpa qui officia deserunt mollit anim id est laborum</p>
    <span class="ref-author">By Daniel K.</span>
  </article>
</main>

<footer class="site-footer">
  <nav class="footer-nav">Home<span class="slash">/</span>For Business<span class="slash">/</span>For Workers<span class="slash">/</span>Reviews<span class="slash">/</span>Contact Us</nav>
  <div class="social" aria-label="Social links"><span></span><span></span><span></span><span></span><span></span></div>
  <p class="copyright">Copyright © 2017 A Hive in Motion. All Rights Reserved</p>
</footer>
</body>
</html>
```